Corvane Solutions Website

Corvane Solutions (CS) provide Analytics & Enterprise Performance Management (EPM) advisory & consultancy services. We are passionate about data and making a difference for our clients by working in partnership with them, helping them on their journey to becoming an Corvane Solution. We deliver insights which give our clients a competitive edge and a much deeper understanding of their organisation.

We need a website which shows who we are, what we do and how we do it.

www.corvane-solutions.com is our very basic website at the moment. We want to completely revamp it with a corporate look

```html
<!DOCTYPE html>
<html lang="en">
<head>
<meta charset="utf-8">
<title>Corvane Solutions</title>
<link href="https://fonts.googleapis.com/css2?family=Roboto:wght@400;500;700;900&family=Lato:wght@400;700&display=swap" rel="stylesheet">
<style>
:root{
  --navy:#1f3a52;
  --navy-dark:#15293b;
  --ink:#1b1f24;
  --text:#4a4f55;
  --light:#eef1f5;
  --white:#ffffff;
  --star:#f2b01e;
}
*{box-sizing:border-box;margin:0;padding:0}
html,body{width:1200px;height:4435px;overflow:hidden}
body{font-family:"Lato",sans-serif;color:var(--text);background:var(--white);position:relative}
.abs{position:absolute}
h1,h2,h3,h4,.label{font-family:"Roboto",sans-serif}
.label{font-size:13px;font-weight:700;color:var(--navy);text-transform:uppercase;letter-spacing:.3px;text-align:center}
.title{font-size:44px;font-weight:700;color:var(--ink);text-align:center;text-transform:uppercase;line-height:1.1;letter-spacing:-.3px}
.rule{width:32px;height:4px;background:var(--navy);margin:10px auto 0}
/* top bar */
.topbar{top:0;left:0;width:1200px;height:38px;background:var(--navy)}
.topbar .social{position:absolute;left:133px;top:6px;display:flex;gap:18px}
.topbar .social span{width:27px;height:27px;border:2px solid #fff;border-radius:50%}
.topbar .contact{position:absolute;left:670px;top:10px;display:flex;gap:36px;color:#fff;font-size:13px;align-items:center}
.topbar .contact div{display:flex;gap:12px;align-items:center}
/* nav */
.nav{top:38px;left:0;width:1200px;height:74px;background:#fff;box-shadow:0 2px 6px rgba(0,0,0,.08)}
.brand{display:flex;align-items:center;gap:10px}
.brand .mark{width:52px;height:52px;border-radius:50%;border:8px solid var(--navy)}
.brand .name{font-family:"Roboto",sans-serif;font-weight:700;color:var(--navy);font-size:18px;line-height:1.05;letter-spacing:.5px;text-transform:uppercase}
.nav .brand{position:absolute;left:80px;top:11px}
.nav ul{position:absolute;left:318px;top:30px;display:flex;gap:30px;list-style:none;font-family:"Roboto",sans-serif;font-size:11px;font-weight:700;color:var(--ink)}
.nav ul li.active{color:var(--navy);border-bottom:3px solid var(--navy);padding-bottom:4px}
.btn{display:inline-block;background:var(--navy);color:#fff;font-family:"Roboto",sans-serif;font-weight:700;border-radius:30px;text-transform:uppercase}
.nav .btn{position:absolute;left:974px;top:14px;width:146px;height:48px;line-height:48px;text-align:center;font-size:14px}
/* hero */
.hero{top:112px;left:0;width:1200px;height:601px;background:linear-gradient(180deg,#4f6a80 0%,#647c8d 45%,#3d4d58 70%,#2d3a44 100%)}
.hero .shade{position:absolute;inset:0;background:rgba(20,40,60,.35)}
.hero .inner{position:absolute;top:194px;left:0;width:1200px;text-align:center;color:#fff}
.hero .kicker{font-family:"Roboto",sans-serif;font-size:14px;font-weight:500;text-transform:uppercase}
.hero h1{font-size:56px;font-weight:700;text-transform:uppercase;margin-top:2px;line-height:1.1}
.hero p{width:820px;margin:6px auto 0;font-size:15px;line-height:28px}
.hero .btn{background:#fff;color:var(--navy);margin-top:16px;padding:0 22px;height:46px;line-height:46px;font-size:15px}
.dots{position:absolute;top:563px;left:568px;display:flex;gap:5px}
.dots span{width:12px;height:12px;border:1.5px solid #fff;border-radius:50%}
.dots span.on{background:#fff}
/* services */
.services{top:713px;left:0;width:1200px;height:618px;background:#fff}
.cards{position:absolute;top:202px;left:128px;display:flex;gap:17px}
.card{width:304px;height:315px;background:#fff;box-shadow:0 4px 16px rgba(0,0,0,.08);border-radius:8px;text-align:center;padding-top:12px}
.card.raised{box-shadow:0 8px 26px rgba(0,0,0,.16)}
.card .ico{width:100px;height:100px;margin:0 auto;border-radius:50%;background:var(--navy);display:flex;align-items:center;justify-content:center}
.card h3{margin-top:16px;font-size:15px;font-weight:700;color:var(--ink);text-transform:uppercase}
.card .rule{width:28px;height:3px;margin-top:10px}
.card p{font-size:13px;line-height:28px;margin:14px 20px 0}
/* about */
.about{top:1331px;left:0;width:1200px;height:584px;background:var(--light)}
.about .photo{position:absolute;left:135px;top:55px;width:460px;height:460px;border-radius:50%;background:linear-gradient(135deg,#7d8e9c,#3e5264 60%,#2a3a48)}
.about .photo::after{content:"";position:absolute;left:170px;top:170px;width:170px;height:120px;background:var(--light);border-radius:0 0 0 0}
.about .copy{position:absolute;left:633px;top:95px;width:440px}
.about .label,.about .title{text-align:left}
.about .title{font-size:42px;margin-top:4px}
.about .rule{margin:8px 0 0}
.about p{font-size:13px;line-height:28px;margin-top:26px;color:var(--text)}
.about p+p{margin-top:28px}
.about .btn{margin-top:14px;width:146px;height:48px;line-height:48px;text-align:center;font-size:14px}
/* clients */
.clients{top:1915px;left:0;width:1200px;height:362px;background:linear-gradient(180deg,#24435e,#1e3850)}
.clients .label,.clients .title{color:#fff}
.logos{position:absolute;top:185px;left:126px;display:flex;gap:20px}
.logos div{width:174px;height:72px;background:#fff;border-radius:4px;display:flex;align-items:center;justify-content:center;gap:8px;font-family:"Roboto",sans-serif;font-weight:700;font-size:13px;color:var(--navy)}
.logos div span{width:14px;height:14px;border-radius:50%;background:var(--navy)}
.logos div.sel{border:2px solid #6b8aa5}
.arrow{position:absolute;top:205px}
/* team */
.team{top:2277px;left:0;width:1200px;height:630px;background:var(--light)}
.people{position:absolute;top:195px;left:110px;display:flex;gap:23px}
.person{width:228px;height:354px;text-align:center;padding-top:8px}
.person.raised{background:#fff;box-shadow:0 6px 20px rgba(0,0,0,.15)}
.person .pic{width:200px;height:200px;border-radius:50%;margin:0 auto;background:linear-gradient(160deg,#b9c4cc,#56697a)}
.person.raised .pic{border:3px solid var(--navy)}
.person h4{margin-top:22px;font-size:16px;font-weight:700;color:var(--ink);letter-spacing:.5px}
.person p{font-size:12px;line-height:28px;margin:4px 14px 0}
/* reviews */
.reviews{top:2907px;left:0;width:1200px;height:560px;background:#fff}
.revs{position:absolute;top:218px;left:144px;display:flex;gap:39px}
.rev{width:437px;height:255px;background:#fff;box-shadow:0 4px 18px rgba(0,0,0,.12);position:relative}
.rev .pic{position:absolute;left:22px;top:25px;width:70px;height:70px;border-radius:50%;background:linear-gradient(160deg,#c8b6a4,#6e5e52)}
.rev .quote{position:absolute;left:32px;top:120px;font-family:Georgia,serif;font-size:100px;color:#a3adb6;line-height:1}
.rev h4{position:absolute;left:138px;top:28px;font-size:17px;font-weight:700;color:var(--navy)}
.rev .role{position:absolute;left:138px;top:52px;font-size:13px}
.rev .stars{position:absolute;left:228px;top:51px;color:var(--star);font-size:13px;letter-spacing:1px}
.rev p{position:absolute;left:140px;top:80px;width:268px;font-size:12px;line-height:28px;text-align:justify}
.sq{position:absolute;left:1036px;top:3363px;width:18px;height:18px;background:#8fa3b5}
/* how */
.how{top:3467px;left:0;width:1200px;height:649px;background:linear-gradient(180deg,#2a4a66,#1d3550 60%,#223d57)}
.how .label,.how .title{color:#fff}
.hcards{position:absolute;top:201px;left:133px;display:flex;gap:21px}
.hcard{width:298px;position:relative;height:365px}
.hcard .pic{height:192px;background:linear-gradient(150deg,#c9d2da,#5d7284);border-radius:4px}
.hcard.sel .pic{border:2px solid #fff;background:linear-gradient(160deg,#3e5f80,#142a40)}
.hcard .box{position:absolute;left:15px;right:15px;top:188px;height:176px;background:#fff;text-align:center;padding-top:14px}
.hcard.sel .box{top:198px;height:176px}
.hcard h3{font-size:15px;font-weight:700;color:var(--ink);text-transform:uppercase;line-height:28px}
.hcard .rule{width:28px;height:3px;margin-top:6px}
.hcard p{font-size:13px;line-height:28px;margin:14px 12px 0;color:var(--ink)}
/* footer */
.footer{top:4116px;left:0;width:1200px;height:319px;background:#fff}
.footer .brand{position:absolute;left:140px;top:92px}
.footer .brand .mark{width:62px;height:62px;border-width:9px}
.footer .brand .name{font-size:21px}
.copy-note{position:absolute;left:124px;top:175px;width:262px;text-align:center;font-size:13px;line-height:24px;color:var(--ink)}
.partner{position:absolute;left:184px;top:226px;display:flex;align-items:center;gap:10px;font-size:12px;color:var(--ink)}
.partner b{font-family:"Lato",sans-serif;font-weight:700;color:#c0392b;font-size:13px;padding-right:10px;border-right:1px solid var(--ink)}
.fcol{position:absolute;top:66px;font-size:13px;color:var(--ink)}
.fcol h4{font-size:14px;font-weight:700;margin-bottom:20px}
.fcol .row{display:flex;gap:14px;align-items:flex-start;line-height:24px;margin-bottom:18px}
.fcol .circ{width:28px;height:28px;border-radius:50%;background:var(--navy);flex:none;display:flex;align-items:center;justify-content:center}
.fcol ul{list-style:none;line-height:28px}
.fcol ul li::before{content:"»";margin-right:16px}
.fcol .soc li::before{content:"";display:inline-block;width:10px;height:10px;background:var(--ink);border-radius:50%;margin-right:16px}
</style>
</head>
<body>

<header class="topbar abs">
  <div class="social"><span></span><span></span><span></span><span></span></div>
  <div class="contact">
    <div><svg width="16" height="16" viewBox="0 0 24 24"><path fill="#fff" d="M6.6 10.8a15 15 0 0 0 6.6 6.6l2.2-2.2c.3-.3.7-.4 1-.2 1.1.4 2.3.6 3.6.6.6 0 1 .4 1 1V20c0 .6-.4 1-1 1A17 17 0 0 1 3 4c0-.6.4-1 1-1h3.5c.6 0 1 .4 1 1 0 1.3.2 2.5.6 3.6.1.3 0 .7-.2 1z"/></svg>01 480 2275</div>
    <div><svg width="16" height="16" viewBox="0 0 24 24"><path fill="#fff" d="M2 11 22 3l-6 18-4-8z"/></svg>info@corvane-solutions.com</div>
  </div>
</header>

<nav class="nav abs">
  <div class="brand"><div class="mark"></div><div class="name">Corvane<br>Solutions</div></div>
  <ul>
    <li class="active">Home</li><li>Who We Are</li><li>What We Do</li><li>How We Do It</li><li>Our Clients</li><li>Reviews</li><li>Our People</li>
  </ul>
  <span class="btn">Get In Touch</span>
</nav>

<section class="hero abs" role="img" aria-label="City waterfront skyline with a modern bridge at dusk">
  <div class="shade"></div>
  <div class="inner">
    <div class="kicker">Data Analytics &amp; EPM Consulting Services</div>
    <h1>Corvane Solutions</h1>
    <p>CS are a Data Analytics &amp; EPM company, specialising in the implementation and support of Business Intelligence, EPM and Data Analytics business solutions, both in the Cloud and on-premise.</p>
    <span class="btn">Get Started</span>
  </div>
  <div class="dots"><span></span><span class="on"></span><span></span><span></span></div>
</section>

<section class="services abs">
  <div style="padding-top:85px">
    <div class="label">Our Services</div>
    <h2 class="title">What We Do</h2>
    <div class="rule"></div>
  </div>
  <div class="cards">
    <div class="card">
      <div class="ico"><svg width="50" height="50" viewBox="0 0 50 50" fill="none" stroke="#fff" stroke-width="2"><circle cx="20" cy="18" r="7"/><path d="M8 42c0-8 5-13 12-13s12 5 12 13"/><rect x="28" y="6" width="16" height="11" rx="2"/></svg></div>
      <h3>Advise &amp; Architect</h3><div class="rule"></div>
      <p>Helping our customers understand the art of the possible and safeguarding their investments by overseeing implementations.</p>
    </div>
    <div class="card raised">
      <div class="ico"><svg width="50" height="50" viewBox="0 0 50 50" fill="none" stroke="#fff" stroke-width="2"><path d="M10 40 30 20"/><circle cx="34" cy="16" r="7"/><path d="M12 12l10 10M8 16l8-8"/></svg></div>
      <h3>Design &amp; Implement</h3><div class="rule"></div>
      <p>Working with the project management team, through each stage of the project, with clearly defined deliverables and well exercised plans to deliver them.</p>
    </div>
    <div class="card">
      <div class="ico"><svg width="50" height="50" viewBox="0 0 50 50" fill="none" stroke="#fff" stroke-width="2"><circle cx="25" cy="25" r="15" stroke-dasharray="5 3"/><circle cx="25" cy="25" r="9"/><path d="M22 21l-4 4 4 4M28 21l4 4-4 4"/></svg></div>
      <h3>Optimise &amp; Manage</h3><div class="rule"></div>
      <p>Our Managed Services delivers proactive, on-demand support for EPM and Data Analytics environments.</p>
    </div>
  </div>
</section>

<section class="about abs">
  <div class="photo" role="img" aria-label="Office building and business meeting photo set in a large rounded frame"></div>
  <div class="copy">
    <div class="label">Who We Are</div>
    <h2 class="title">About Corvane Solutions</h2>
    <div class="rule"></div>
    <p>Corvane Solutions is an exciting start-up in the Data Analytics and EPM space. Founded in 2019, CS specialise in the implementation and support of BI, EPM and Data Analytics business solutions, both in the Cloud and on-premise.</p>
    <p>Call us on 01 480 2275 or email: info@corvane-solutions.com for more information</p>
    <span class="btn">Learn More</span>
  </div>
</section>

<section class="clients abs">
  <div style="padding-top:68px">
    <div class="label">Partners</div>
    <h2 class="title">Our Clients Partner</h2>
    <div class="rule" style="background:#fff"></div>
  </div>
  <svg class="arrow" style="left:76px" width="20" height="30" viewBox="0 0 20 30"><path d="M15 3 4 15l11 12" fill="none" stroke="#fff" stroke-width="2"/></svg>
  <div class="logos">
    <div><span></span>Starline</div>
    <div><span></span>Bizcore</div>
    <div class="sel"><span></span>Apexa</div>
    <div><span></span>Novara</div>
    <div><span></span>Crestia</div>
  </div>
  <svg class="arrow" style="left:1104px" width="20" height="30" viewBox="0 0 20 30"><path d="M5 3l11 12L5 27" fill="none" stroke="#fff" stroke-width="2"/></svg>
</section>

<section class="team abs">
  <div style="padding-top:80px">
    <div class="label">Team</div>
    <h2 class="title">Meet Our People</h2>
    <div class="rule"></div>
  </div>
  <div class="people">
    <div class="person"><div class="pic" role="img" aria-label="Portrait of team member"></div><h4>DANIEL HART</h4><p>Lorem ipsum dolor sit amet, consectetur adipiscing elit, sed do eiusmod tempo.</p></div>
    <div class="person raised"><div class="pic" role="img" aria-label="Portrait of team member"></div><h4>DANIEL HART</h4><p>Lorem ipsum dolor sit amet, consectetur adipiscing elit, sed do eiusmod tempo.</p></div>
    <div class="person"><div class="pic" role="img" aria-label="Portrait of team member"></div><h4>DANIEL HART</h4><p>Lorem ipsum dolor sit amet, consectetur adipiscing elit, sed do eiusmod tempo.</p></div>
    <div class="person"><div class="pic" role="img" aria-label="Portrait of team member"></div><h4>DANIEL HART</h4><p>Lorem ipsum dolor sit amet, consectetur adipiscing elit, sed do eiusmod tempo.</p></div>
  </div>
</section>

<section class="reviews abs">
  <div style="padding-top:90px">
    <div class="label">Reviews</div>
    <h2 class="title">What Our Clients Say</h2>
    <div class="rule"></div>
  </div>
  <div class="revs">
    <div class="rev"><div class="pic" role="img" aria-label="Client portrait"></div><div class="quote">“</div><h4>Liam Ford</h4><div class="role">Lorem Ipsum set</div><div class="stars">★★★★★</div><p>Nemo enim ipsam voluptatem quia voluptas sit aspernatur aut odit aut fugit, sed quia consequuntur magni dolores eos qui ratione voluptatem sequi nesciunt aut fugit, sed quia consequuntur magni.</p></div>
    <div class="rev"><div class="pic" role="img" aria-label="Client portrait"></div><div class="quote">“</div><h4>Liam Ford</h4><div class="role">Lorem Ipsum set</div><div class="stars">★★★★★</div><p>Nemo enim ipsam voluptatem quia voluptas sit aspernatur aut odit aut fugit, sed quia consequuntur magni dolores eos qui ratione voluptatem sequi nesciunt aut fugit, sed quia consequuntur magni.</p></div>
  </div>
</section>
<div class="sq"></div>

<section class="how abs" role="img" aria-label="Business handshake background in deep blue tones">
  <div style="padding-top:88px">
    <div class="label">Lorem Ipsum Dolor</div>
    <h2 class="title">How We Do It</h2>
    <div class="rule" style="background:#fff"></div>
  </div>
  <div class="hcards">
    <div class="hcard"><div class="pic" role="img" aria-label="Analytics charts on a desk"></div><div class="box"><h3>Analytics</h3><div class="rule"></div><p>Lorem ipsum dolor sit amet, consectetur adipiscing elit, sed do eiusmod tempor incididunt ut labore .</p></div></div>
    <div class="hcard sel"><div class="pic" role="img" aria-label="Businessman with rising growth arrows"></div><div class="box"><h3>Enterprise Performance Management</h3><div class="rule"></div><p>Lorem ipsum dolor sit amet, consectetur adipiscing elit, sed do eiusmod tempor incididunt ut labore .</p></div></div>
    <div class="hcard"><div class="pic" role="img" aria-label="Consultant meeting a client in an office"></div><div class="box"><h3>Advisory &amp; Consultancy</h3><div class="rule"></div><p>Lorem ipsum dolor sit amet, consectetur adipiscing elit, sed do eiusmod tempor incididunt ut labore .</p></div></div>
  </div>
</section>

<footer class="footer abs">
  <div class="brand"><div class="mark"></div><div class="name">Corvane<br>Solutions</div></div>
  <div class="copy-note">© copyrights 2022 Corvane Solutions<br>All rights reserved.</div>
  <div class="partner"><b>VELTRIX</b>Partner</div>
  <div class="fcol" style="left:438px;width:270px">
    <h4>CONTACT US</h4>
    <div class="row"><span class="circ"><svg width="12" height="14" viewBox="0 0 12 16"><path fill="#fff" d="M6 0a6 6 0 0 0-6 6c0 4 6 10 6 10s6-6 6-10a6 6 0 0 0-6-6zm0 8a2 2 0 1 1 0-4 2 2 0 0 1 0 4z"/></svg></span><span>14 Harbour Row, Westmere,<br>Dublin 4, D04 KR21</span></div>
    <div class="row" style="align-items:center"><span class="circ"><svg width="12" height="12" viewBox="0 0 24 24"><path fill="#fff" d="M6.6 10.8a15 15 0 0 0 6.6 6.6l2.2-2.2c.3-.3.7-.4 1-.2 1.1.4 2.3.6 3.6.6.6 0 1 .4 1 1V20c0 .6-.4 1-1 1A17 17 0 0 1 3 4c0-.6.4-1 1-1h3.5c.6 0 1 .4 1 1 0 1.3.2 2.5.6 3.6.1.3 0 .7-.2 1z"/></svg></span>01 480 2275</div>
    <div class="row" style="align-items:center"><span class="circ"><svg width="14" height="10" viewBox="0 0 14 10"><rect width="14" height="10" rx="1" fill="#fff"/><path d="M0 1l7 5 7-5" fill="none" stroke="#1f3a52"/></svg></span>info@corvane-solutions.com</div>
  </div>
  <div class="fcol" style="left:740px">
    <h4>QUICK LINKS</h4>
    <ul><li>Home</li><li>Who We Are</li><li>What We Do</li><li>How We Do It</li><li>Our Clients</li><li>More</li></ul>
  </div>
  <div class="fcol" style="left:955px">
    <h4>FOLLOW US</h4>
    <ul class="soc" style="line-height:36px"><li>Linkora</li><li>Snapfeed</li><li>Chirpa</li><li>Streamly</li></ul>
  </div>
</footer>

</body>
</html>
```